Safety Brochure for Industry Assocations

This is an 8.5 x 11 single sided brochure for our Occupational Health and Safety Data Analytics software. If you need to use stock images we will pay for them.

Please incorporate our logo and some of the images. No need to incorporate them all. We like the idea of the boots being at the bottom of the page but we're open to other ideas.

Please note that we intend to mail this brochure to different industries so it should be generic (i.e. not construction specific).

Target Market(s)

Safety and Industry Organisations for construction, mining, forestry and oil and gas industries.

Industry/Entity Type

Industry

Font styles to use
Sans Serif

Colors

Designer to choose colors to be used in the design.

Requirements
Must have
• We are a software company that produces safety software. Our customers are companies that engage in dangerous work and use our software to improve their worker's safety. The look and feel should convey the fact that:
• -We are Big Data
• -We are Software
• -We service industry
Nice to have
• Please see the Pixlore photo of the boots. We were hoping that the desiger would be able ti modify the image with an overlay of 0's and 1's in a kind of "matrix" fashion to indicate that we are merging traditional labour work with software.
Should not have
• No medical symbols. Note that WE ARE NOT HEALTH CARE.

```html
<!DOCTYPE html>
<html lang="en">
<head>
<meta charset="utf-8">
<title>Northline Metrics – Leverage the power of Big Data</title>
<link rel="stylesheet" href="https://fonts.googleapis.com/css2?family=Lato:wght@400;700;900&family=Roboto+Condensed:wght@700;900&display=swap">
<style>
  :root {
    --green: #7cb342;
    --green-dark: #4f9a2c;
    --lime: #a6cf3c;
    --charcoal: #3a3a3a;
    --grey: #6d6d6d;
    --line: #bdbdbd;
    --paper: #ffffff;
    --paper-shade: #f1f1f1;
    --backdrop: #e6e6e4;
  }
  * { box-sizing: border-box; margin: 0; padding: 0; }
  html, body { width: 1200px; height: 984px; overflow: hidden; background: var(--backdrop); }
  body { font-family: "Lato", sans-serif; color: var(--charcoal); }

  .flyer {
    position: absolute; left: 229px; top: 12px; width: 742px; height: 960px;
    background: linear-gradient(180deg, var(--paper) 0%, var(--paper-shade) 100%);
    box-shadow: 0 8px 24px rgba(0,0,0,.18); overflow: hidden;
  }

  /* header */
  .header-photo { position: absolute; right: 0; top: 0; width: 460px; height: 214px; }
  .brand { position: absolute; left: 38px; top: 34px; display: flex; align-items: center; gap: 10px; }
  .brand-dot { width: 34px; height: 34px; border-radius: 50%; background: var(--green); }
  .brand-name { font-family: "Lato", sans-serif; font-weight: 700; font-size: 19px; color: var(--grey); letter-spacing: 1px; }
  .headline { position: absolute; left: 38px; top: 96px; }
  .headline-lead { font-family: "Lato", sans-serif; font-weight: 700; font-size: 25px; color: var(--grey); }
  .headline-big { font-family: "Roboto Condensed", sans-serif; font-weight: 900; font-size: 58px; line-height: 1; color: var(--green); letter-spacing: 1px; }

  .divider { position: absolute; left: 0; top: 214px; width: 100%; height: 6px; display: flex; }
  .divider-green { flex: 0 0 42%; background: var(--lime); }
  .divider-dark { flex: 1; background: var(--charcoal); }

  /* benefits */
  .benefit { position: absolute; display: flex; align-items: center; gap: 12px; font-size: 13px; color: var(--grey); line-height: 1.2; }
  .benefit strong { font-weight: 400; color: var(--charcoal); letter-spacing: .5px; }
  .benefit-icon { flex: 0 0 34px; height: 34px; border-radius: 50%; border: 3px solid var(--charcoal); background: var(--green-dark); display: grid; place-items: center; }

  /* diagram */
  .diagram { position: absolute; left: 40px; top: 400px; width: 662px; height: 250px; }
  .data-cloud-label { position: absolute; left: 0; width: 662px; top: 26px; text-align: center; font-family: "Roboto Condensed", sans-serif; font-weight: 700; font-size: 17px; color: #fff; }
  .pillars { position: absolute; left: 0; top: 104px; width: 662px; display: grid; grid-template-columns: 1fr 1.25fr 1fr;
    border: 2px solid var(--line); border-radius: 14px; overflow: hidden; background: var(--paper); }
  .pillar { border-left: 1.5px solid var(--line); }
  .pillar:first-child { border-left: 0; }
  .pillar-title { background: var(--lime); text-align: center; font-family: "Roboto Condensed", sans-serif; font-weight: 700; font-size: 13px; color: var(--charcoal); padding: 8px 0; }
  .pillar-row { text-align: center; font-size: 12px; font-weight: 700; color: var(--charcoal); padding: 8px 4px; border-top: 1.5px solid var(--line); }
  .pillar-row:last-child { padding-bottom: 14px; }

  /* tagline + boots */
  .boots { position: absolute; right: 0; top: 640px; width: 300px; height: 210px; }
  .tagline { position: absolute; left: 40px; top: 720px; }
  .tagline-main { font-family: "Roboto Condensed", sans-serif; font-weight: 700; font-size: 26px; color: #1f1f1f; }
  .tagline-main b { font-weight: 900; font-size: 30px; }
  .tagline-sub { font-family: "Roboto Condensed", sans-serif; font-weight: 700; font-size: 24px; color: var(--green); }

  /* footer */
  .footer-band { position: absolute; left: 0; bottom: 0; width: 742px; height: 150px; }
  .contact { position: absolute; left: 40px; bottom: 22px; color: #fff; font-size: 12.5px; }
  .contact li { list-style: none; display: flex; align-items: center; gap: 10px; margin-top: 6px; }
  .contact .phone { font-family: "Roboto Condensed", sans-serif; font-weight: 700; font-size: 19px; }
  .contact-icon { width: 14px; height: 14px; border-radius: 50%; background: #fff; display: grid; place-items: center; }
</style>
</head>
<body>
<main class="flyer">

  <svg class="header-photo" viewBox="0 0 460 214" role="img" aria-label="Photo of a tablet beneath cloud icons linked to connected devices">
    <defs>
      <linearGradient id="photoTone" x1="0" y1="0" x2="1" y2="1">
        <stop offset="0" stop-color="#e9eef3"/>
        <stop offset=".55" stop-color="#8fb3d8"/>
        <stop offset="1" stop-color="#2f63a8"/>
      </linearGradient>
    </defs>
    <polygon points="40,0 460,0 460,120 330,214 0,214 0,0" fill="url(#photoTone)"/>
    <polygon points="460,95 460,125 335,214 300,214" fill="var(--green)"/>
  </svg>

  <div class="brand">
    <span class="brand-dot"></span>
    <span class="brand-name">Northline Metrics</span>
  </div>

  <div class="headline">
    <p class="headline-lead">Leverage the power of</p>
    <p class="headline-big">BIG DATA!</p>
  </div>

  <div class="divider"><span class="divider-green"></span><span class="divider-dark"></span></div>

  <div class="benefit" style="left:40px; top:268px;">
    <span class="benefit-icon"><svg width="16" height="16" viewBox="0 0 16 16"><circle cx="5" cy="4" r="2" fill="#fff"/><circle cx="11" cy="4" r="2" fill="#fff"/><rect x="3" y="7" width="4" height="7" fill="#fff"/><rect x="9" y="7" width="4" height="7" fill="#fff"/></svg></span>
    <span><strong>LEAD</strong> the next wave of injury reduction</span>
  </div>
  <div class="benefit" style="left:40px; top:314px;">
    <span class="benefit-icon"><svg width="16" height="16" viewBox="0 0 16 16"><path d="M3 8a5 5 0 0 1 9-3M13 8a5 5 0 0 1-9 3" stroke="#fff" stroke-width="2" fill="none"/></svg></span>
    <span><strong>ENGAGE</strong> with members through collaboration<br>and benchmarking</span>
  </div>
  <div class="benefit" style="left:40px; top:360px;">
    <span class="benefit-icon"><svg width="16" height="16" viewBox="0 0 16 16"><rect x="2" y="3" width="12" height="8" fill="none" stroke="#fff" stroke-width="2"/><path d="M8 11v3" stroke="#fff" stroke-width="2"/></svg></span>
    <span><strong>PROMOTE</strong> standardization</span>
  </div>
  <div class="benefit" style="left:400px; top:248px;">
    <span class="benefit-icon"><svg width="16" height="16" viewBox="0 0 16 16"><circle cx="7" cy="7" r="4" fill="none" stroke="#fff" stroke-width="2"/><path d="M10 10l4 4" stroke="#fff" stroke-width="2"/></svg></span>
    <span><strong>ANALYZE</strong> Accurate, Timely and Complete<br>Leading Indicators</span>
  </div>
  <div class="benefit" style="left:400px; top:294px;">
    <span class="benefit-icon"><svg width="16" height="16" viewBox="0 0 16 16"><rect x="5" y="2" width="9" height="7" fill="none" stroke="#fff" stroke-width="2"/><circle cx="4" cy="10" r="2" fill="#fff"/><rect x="2" y="12" width="4" height="3" fill="#fff"/></svg></span>
    <span><strong>TRAIN</strong> industry more proactively</span>
  </div>

  <section class="diagram">
    <svg width="662" height="110" viewBox="0 0 662 110" style="position:absolute;left:0;top:0">
      <path d="M110 104V82H552V104M331 82V64" stroke="#333" stroke-width="2" fill="none"/>
      <path d="M290 66a18 18 0 0 1 6-34a24 24 0 0 1 44-10a20 20 0 0 1 32 18a14 14 0 0 1 0 26z" fill="var(--charcoal)"/>
    </svg>
    <p class="data-cloud-label">EHS Data</p>
    <div class="pillars">
      <div class="pillar">
        <p class="pillar-title">TRAINING</p>
        <p class="pillar-row">Analyze needs of Industry</p>
        <p class="pillar-row">Deliver Proactive Training</p>
        <p class="pillar-row">Improve Safety</p>
      </div>
      <div class="pillar">
        <p class="pillar-title">BENCHMARKING</p>
        <p class="pillar-row">Engage with Members</p>
        <p class="pillar-row">Promote Collaborative Advancement of Safety</p>
        <p class="pillar-row">Improve Safety</p>
      </div>
      <div class="pillar">
        <p class="pillar-title">TREND ANALYSIS</p>
        <p class="pillar-row">Monitor Industry Trends</p>
        <p class="pillar-row">Implement Corrective Initiatives</p>
        <p class="pillar-row">Improve Safety</p>
      </div>
    </div>
  </section>

  <svg class="boots" viewBox="0 0 300 210" role="img" aria-label="Pair of work boots overlaid with green binary digits">
    <defs>
      <radialGradient id="bootTone" cx=".55" cy=".55" r=".6">
        <stop offset="0" stop-color="#5fbf3a"/>
        <stop offset=".7" stop-color="#2f7a1f"/>
        <stop offset="1" stop-color="#2f7a1f" stop-opacity="0"/>
      </radialGradient>
    </defs>
    <rect width="300" height="210" fill="url(#bootTone)"/>
  </svg>

  <div class="tagline">
    <p class="tagline-main">The next <b>BIG STEP</b> in injury reduction!</p>
    <p class="tagline-sub">FOR YOUR ENTIRE INDUSTRY</p>
  </div>

  <svg class="footer-band" viewBox="0 0 742 150" preserveAspectRatio="none">
    <polygon points="0,18 742,8 742,0 0,12" fill="var(--charcoal)"/>
    <polygon points="0,22 742,12 742,150 0,150" fill="var(--green)"/>
  </svg>
  <ul class="contact">
    <li class="phone"><span class="contact-icon"><svg width="8" height="8" viewBox="0 0 8 8"><path d="M1 1h2l1 2-1 1a4 4 0 0 0 2 2l1-1 2 1v2A7 7 0 0 1 1 1z" fill="var(--green)"/></svg></span>1-888-555-0142</li>
    <li><span class="contact-icon"><svg width="8" height="8" viewBox="0 0 8 8"><rect x="0" y="1.5" width="8" height="5" fill="var(--green)"/></svg></span>info@northlinemetrics.com</li>
    <li><span class="contact-icon"><svg width="8" height="8" viewBox="0 0 8 8"><circle cx="4" cy="4" r="3" fill="none" stroke="var(--green)" stroke-width="1.4"/></svg></span>www.northlinemetrics.com</li>
    <li><span class="contact-icon"><svg width="8" height="8" viewBox="0 0 8 8"><path d="M4 8L1.5 4a2.5 2.5 0 1 1 5 0z" fill="var(--green)"/></svg></span>Suite # 210 - 118 Harbour Ave Fairview AB T0H 1L0</li>
  </ul>

</main>
</body>
</html>
```